Business card for STEADYWAVE

Please design professional business card for IT consulting firm STEADYWAVE INC.
Use logo attached.
Use information from sample qNode business card attached.
replace qnode inc with STEADYWAVE INC.
as well as qnodeinc.com with steadywave.example

```html
<!DOCTYPE html>
<html lang="en">
<head>
<meta charset="utf-8">
<title>STEADYWAVE INC. – Business Card</title>
<link rel="stylesheet" href="https://fonts.googleapis.com/css2?family=Source+Sans+3:wght@300;400;700&display=swap">
<style>
  :root {
    --backdrop: #2b2b2d;
    --card: #ececee;
    --ink: #161618;
    --ink-soft: #3a3a3e;
    --accent: #7a4fd6;
  }
  * { margin: 0; padding: 0; box-sizing: border-box; }
  html, body {
    width: 1200px; height: 801px; overflow: hidden;
    background: var(--backdrop);
    font-family: "Source Sans 3", sans-serif;
  }
  .stage {
    width: 1200px; height: 801px;
    display: flex; align-items: center; justify-content: center;
  }
  .business-card {
    position: relative;
    width: 980px; height: 560px;
    background: var(--card);
    border-radius: 34px;
    color: var(--ink);
  }
  .brand {
    position: absolute; left: 72px; top: 62px;
    display: flex; align-items: center; gap: 18px;
  }
  .brand-name {
    font-size: 66px; font-weight: 700; letter-spacing: 6px;
    line-height: 1; color: var(--ink);
  }
  .brand-mark {
    width: 30px; height: 30px; background: var(--accent);
  }
  .job-title {
    position: absolute; left: 160px; top: 196px;
    font-size: 34px; font-weight: 300; letter-spacing: 1px;
    color: var(--ink-soft);
  }
  .person-name {
    position: absolute; left: 145px; top: 236px;
    font-size: 38px; font-weight: 400; letter-spacing: 0.5px;
  }
  .contact {
    position: absolute; font-size: 19px; line-height: 32px;
    color: var(--ink-soft); list-style: none;
  }
  .contact-phones { left: 130px; top: 306px; }
  .contact-online { left: 400px; top: 318px; }
  .office {
    position: absolute; left: 112px; top: 392px; color: var(--ink);
  }
  .office-name { font-size: 34px; font-weight: 400; line-height: 1.1; }
  .office-address { font-size: 20px; line-height: 26px; font-style: normal; }
</style>
</head>
<body>
<main class="stage">
  <article class="business-card">
    <header class="brand">
      <span class="brand-name">STEADYWAVE INC</span>
      <span class="brand-mark" aria-hidden="true"></span>
    </header>

    <p class="job-title">GENERAL MANAGER</p>
    <h1 class="person-name">DANIEL MORROW, P.ENG</h1>

    <ul class="contact contact-phones">
      <li>o. (555)014-2200 ext.201</li>
      <li>e. (555) 019-3371</li>
    </ul>
    <ul class="contact contact-online">
      <li>c. dmorrow@steadywave.example</li>
      <li>www.steadywave.example</li>
    </ul>

    <section class="office">
      <p class="office-name">Steadywave inc</p>
      <address class="office-address">
        1820 Harbor Line Rd, Suite 101<br>
        Lakeview, Ontario, L0A 1B2, canada
      </address>
    </section>
  </article>
</main>
</body>
</html>
```